World Wide News and Current Affairs website

We intends to start up a new website which deals on New and Current Affairs.
Attention Designers,
We want a home page design for this project. Our business is based in the United States. Our goal is to become a well known brand.
The website would consist of a category for News, Business and Tech.
The theme should be beautiful and attention seeking. The website would take bulk of it's news from the US, and Europe.
Designers can get inspiration from already existing new websites such as HVZ, FQJ, DORNAKE.
All designs should be clean and easy to navigate.

```html
<!DOCTYPE html>
<html lang="en">
<head>
<meta charset="utf-8">
<title>World News Home</title>
<link rel="stylesheet" href="https://fonts.googleapis.com/css2?family=Exo+2:wght@400;500;600&family=Open+Sans:wght@400;600&display=swap">
<style>
:root{
  --red:#c8102e;
  --dark:#2e2e2e;
  --ink:#1a1a1a;
  --muted:#666;
  --line:#ddd;
  --white:#fff;
  --band:#333;
}
*{box-sizing:border-box;margin:0;padding:0}
html,body{width:669px;height:1200px;overflow:hidden;background:var(--white)}
body{position:relative;font-family:"Open Sans",sans-serif;color:var(--ink)}
.abs{position:absolute}
.top-rule{left:0;top:0;width:669px;height:3px;background:var(--red)}
.logo{left:44px;top:14px;font-family:"Exo 2",sans-serif;font-weight:600;font-size:14px;line-height:16px;color:var(--red)}
.logo-rule{left:97px;top:15px;width:1px;height:30px;background:var(--red)}
.dateline{left:108px;top:18px;font-family:"Exo 2",sans-serif;font-size:10px;line-height:11px}
.dateline small{display:block;font-size:7px;color:var(--red);font-weight:600}
.util{top:16px;text-align:center;font-size:8px;color:var(--ink)}
.util svg{display:block;margin:0 auto 2px}
.search{left:400px;top:22px;width:146px;height:16px;border:1px solid #999;font-size:8px;padding:2px 0 0 18px;color:#555}
.search svg{position:absolute;left:4px;top:2px}
.social{top:22px;width:16px;height:16px;background:var(--dark);border-radius:3px}
.nav{left:0;top:58px;width:669px;height:22px;background:var(--dark);display:flex;align-items:center;padding-left:30px}
.nav a{color:var(--white);font-size:7px;font-weight:600;text-decoration:none;padding:0 8px;border-right:1px solid #888;line-height:12px}
.nav a.live{color:var(--red)}
.nav a:last-child{border:none}
.home{left:4px;top:60px}
.menu{left:5px;top:86px}
.ph{background:linear-gradient(135deg,#6b5a4e,#2c2c33)}
.cap{font-size:9px;line-height:12px;color:var(--ink)}
.lead-title{left:41px;top:279px;width:275px;font-size:13px;line-height:17px;font-weight:400}
.lead-text{left:41px;top:318px;width:276px;font-size:6.8px;line-height:10px}
.money{left:30px;top:366px;width:609px;height:53px;background:var(--band);color:var(--white);display:flex;align-items:center}
.money-tag{width:22px;transform:rotate(-90deg);font-size:7px;letter-spacing:1px}
.money-rates{font-family:"Exo 2",sans-serif;font-size:13.5px;padding-left:6px;white-space:nowrap}
.money-rates span{border-right:2px solid var(--white);padding:0 7px}
.money-rates span:last-child{border:none}
.slide-title{left:41px;top:676px;width:433px;height:26px;background:rgba(30,30,30,.75);color:var(--white);font-family:"Exo 2",sans-serif;font-weight:600;font-size:17.5px;line-height:22px;padding:2px 0 0 4px;white-space:nowrap;overflow:hidden}
.wire{left:484px;top:432px;width:147px;height:270px;background:#f2f2f2;overflow:hidden}
.wire-head{height:34px;background:var(--band);color:var(--white);font-family:"Exo 2",sans-serif;font-size:13px;padding:5px 0 0 4px;position:relative}
.wire-head::after{content:"";position:absolute;left:4px;right:6px;bottom:5px;height:1px;background:var(--white)}
.wire-item{margin:10px 12px 0 7px;padding-bottom:12px;border-bottom:1px solid var(--line)}
.wire-item time{display:block;font-size:6.5px;color:var(--muted);margin-bottom:3px}
.wire-item p{font-family:"Exo 2",sans-serif;font-size:7.5px;line-height:11.5px}
.sec-bar{height:17px;background:var(--band);color:var(--white);font-size:8px;padding:3px 0 0 6px}
.card-cap{font-size:9.5px;line-height:13px;color:#555}
.ad{left:470px;top:851px;width:160px;height:150px;background:linear-gradient(180deg,#cfe3ea,#f3f3ea)}
.ad-copy{left:478px;top:897px;font-size:6.5px;line-height:9px;color:#333}
.ad-brand{left:492px;top:966px;font-family:"Exo 2",sans-serif;font-weight:600;font-size:12px;color:var(--ink)}
.ad-dot{left:478px;top:969px;width:10px;height:10px;border-radius:50%;background:#f2c200}
.ad-btn{left:569px;top:964px;width:51px;height:15px;background:#4cae3f;color:var(--white);font-size:8px;text-align:center;line-height:15px}
.ad-note{left:528px;top:986px;font-size:5px;color:#777}
.foot{left:0;top:1008px;width:669px;height:138px;background:var(--red);color:var(--white);display:flex;justify-content:space-around;padding:14px 6px 0}
.foot-col{text-align:center;font-size:8.5px;line-height:11.3px}
.foot-col h3{font-family:"Exo 2",sans-serif;font-weight:400;font-size:14.5px;line-height:14px;margin-bottom:1px}
.legal{left:0;top:1146px;width:669px;height:54px;background:var(--band);color:var(--white);text-align:center;font-size:8.4px;line-height:11.5px;padding-top:10px}
</style>
</head>
<body>
<header>
  <div class="abs top-rule"></div>
  <div class="abs logo">YOUR<br>LOGO</div>
  <div class="abs logo-rule"></div>
  <div class="abs dateline">21 APRIL 2017<small>Washington ☂ 11°</small></div>
  <div class="abs util" style="left:192px"><svg width="10" height="10" viewBox="0 0 10 10"><circle cx="5" cy="5" r="4.3" fill="none" stroke="#c8102e"/><rect x="4.4" y="4" width="1.2" height="3.5" fill="#c8102e"/><circle cx="5" cy="2.8" r=".7" fill="#c8102e"/></svg>about us</div>
  <div class="abs util" style="left:252px"><svg width="12" height="11" viewBox="0 0 12 11"><path d="M6 .5l1.5 3.4 3.7.3-2.8 2.4.9 3.7L6 8.4 2.7 10.3l.9-3.7L.8 4.2l3.7-.3z" fill="none" stroke="#c8102e"/></svg>advertisement</div>
  <div class="abs util" style="left:336px"><svg width="14" height="10" viewBox="0 0 14 10"><path d="M1 5l10-4 2 3-10 4z" fill="none" stroke="#c8102e"/><path d="M2 7l10-4" stroke="#c8102e"/></svg>newsletters</div>
  <div class="abs search"><svg width="8" height="11" viewBox="0 0 8 11"><circle cx="4" cy="4" r="3" fill="none" stroke="#c8102e" stroke-width="1.3"/><path d="M4 7v4" stroke="#c8102e" stroke-width="1.3"/></svg>Search</div>
  <div class="abs social" style="left:554px"></div>
  <div class="abs social" style="left:577px"></div>
  <div class="abs social" style="left:600px"></div>
  <nav class="abs nav">
    <a class="live">LAST MINUTE</a><a>MARKETS</a><a>WORLD</a><a>POLITICS</a><a>TECH</a><a>COMMENTARY</a><a>BREAKING VIEWS</a><a>MONEY</a><a>LIFE</a><a>▭ PICTURES</a><a>▭ VIDEO</a>
  </nav>
  <svg class="abs home" width="20" height="18" viewBox="0 0 20 18"><path d="M10 1L1 9h3v8h4v-5h4v5h4V9h3z" fill="#fff"/></svg>
  <svg class="abs menu" width="18" height="14" viewBox="0 0 18 14"><rect y="0" width="18" height="2.6" fill="#222"/><rect y="5.5" width="18" height="2.6" fill="#222"/><rect y="11" width="18" height="2.6" fill="#222"/></svg>
</header>

<main>
  <section class="top-stories">
    <div class="abs ph" style="left:37px;top:90px;width:278px;height:185px" role="img" aria-label="Photo of the president speaking at a lectern"></div>
    <h1 class="abs lead-title">Squabbles that sank health plan once could do it again</h1>
    <p class="abs lead-text">President Harlan Vosk, striving to make good on a top campaign promise, is pushing Republicans to pass revamped healthcare legislation, but the same intraparty squabbling that torpedoed it last month could do it again.</p>

    <div class="abs ph" style="left:322px;top:90px;width:151px;height:100px;background:linear-gradient(135deg,#8a9bb0,#2e3a55)" role="img" aria-label="Photo of an official rubbing his eyes"></div>
    <p class="abs cap" style="left:322px;top:195px;width:151px">Dale Pruitt 'reminded' Hawaii is a state</p>
    <div class="abs ph" style="left:481px;top:90px;width:151px;height:100px;background:linear-gradient(160deg,#000,#111 55%,#7a7a78)" role="img" aria-label="Photo of the Earth rising over the Moon's surface"></div>
    <p class="abs cap" style="left:481px;top:195px;width:151px">14 April 1970, the crew of Orion 9</p>

    <div class="abs ph" style="left:322px;top:228px;width:151px;height:99px;background:linear-gradient(135deg,#3f4a3a,#c9a8a6)" role="img" aria-label="Photo of the monarch in a pink hat at the races"></div>
    <p class="abs cap" style="left:322px;top:331px;width:151px">Monarch spends birthday at Ashbrook Downs</p>
    <div class="abs ph" style="left:481px;top:228px;width:151px;height:99px;background:linear-gradient(135deg,#b9a585,#6b5e50)" role="img" aria-label="Photo of a woman in a red dress outside parliament"></div>
    <p class="abs cap" style="left:481px;top:331px;width:151px">Petition for work dress code law rejected</p>
  </section>

  <section class="abs money">
    <span class="money-tag">MONEY</span>
    <div class="money-rates"><span>Euro: $1.07 - 0.1312%</span><span>British Pound: $1.28 - 0.0554%</span><span>Japanese Yen: ¥109.10 - 0.1894%</span></div>
  </section>

  <section class="feature">
    <div class="abs ph" style="left:41px;top:432px;width:433px;height:270px;background:linear-gradient(135deg,#3b3c3e,#151617 60%,#4b4a47)" role="img" aria-label="Photo of armed riot police on a street at night"></div>
    <svg class="abs" style="left:45px;top:543px" width="36" height="34" viewBox="0 0 36 34"><path d="M2 17L18 2v9h16v12H18v9z" fill="#fff"/></svg>
    <svg class="abs" style="left:432px;top:543px" width="36" height="34" viewBox="0 0 36 34"><path d="M34 17L18 2v9H2v12h16v9z" fill="#fff"/></svg>
    <h2 class="abs slide-title">Marchand demands closure of all Islamist mosques</h2>

    <aside class="abs wire">
      <div class="wire-head">THE WIRE<svg style="position:absolute;right:8px;top:9px" width="8" height="13" viewBox="0 0 8 13"><path d="M1 1l6 5.5L1 12" fill="none" stroke="#fff" stroke-width="1.5"/></svg></div>
      <div class="wire-item"><time>◷ 13m ago</time><p>Death toll in Afghan base attack rises to 140, officials say</p></div>
      <div class="wire-item"><time>◷ 20m ago</time><p>Islamic State-linked Sulu Front leader killed on Philippine resort island: army</p></div>
      <div class="wire-item"><time>◷ 48m ago</time><p>Thousands of ex-Taliban fighters may have entered Germany: report</p></div>
      <div class="wire-item"><time>◷ 1h ago</time><p>Peaceful outcome for Korean talks still on the table</p></div>
    </aside>
  </section>

  <section class="markets">
    <div class="abs sec-bar" style="left:41px;top:711px;width:589px">MARKETS</div>
    <div class="abs ph" style="left:41px;top:734px;width:137px;height:76px;background:linear-gradient(90deg,#2a4c8c,#e6e6e6 50%,#c8202e)" role="img" aria-label="Photo of two candidates before flags"></div>
    <p class="abs card-cap" style="left:41px;top:815px;width:137px">The election 'nightmare' that could smash the euro</p>
    <div class="abs ph" style="left:192px;top:734px;width:137px;height:76px;background:linear-gradient(180deg,#bfdde0,#d9e6d6)" role="img" aria-label="Illustration of candidate portraits around flags"></div>
    <p class="abs card-cap" style="left:192px;top:815px;width:137px">The beginner's guide to the French elections</p>
    <div class="abs ph" style="left:342px;top:734px;width:137px;height:76px;background:linear-gradient(135deg,#c8303a,#e8e8ee 55%,#3a5aa0)" role="img" aria-label="Photo of a rally crowd waving flags"></div>
    <p class="abs card-cap" style="left:342px;top:815px;width:137px">Opinion: Win or lose, Marchand is a nightmare for EU</p>
    <div class="abs ph" style="left:492px;top:734px;width:137px;height:76px;background:linear-gradient(135deg,#2d4fa0,#e2c23a 55%,#3a5aa0)" role="img" aria-label="Illustration of European politicians with speech bubbles"></div>
    <p class="abs card-cap" style="left:492px;top:815px;width:110px">What's wrong with Europe?</p>
  </section>

  <section class="life">
    <div class="abs sec-bar" style="left:41px;top:852px;width:161px">LIFE</div>
    <div class="abs ph" style="left:41px;top:872px;width:161px;height:88px;background:linear-gradient(135deg,#5d6e48,#2a3346)" role="img" aria-label="Photo of young royals talking at a picnic table"></div>
    <p class="abs card-cap" style="left:41px;top:964px;width:150px;font-size:10px;line-height:13px">Young royals open up about mental health</p>
    <p class="abs" style="left:41px;top:997px;font-size:6.5px;color:#888">Twin drone strikes hit inside ▷</p>
  </section>

  <section class="commentary">
    <div class="abs sec-bar" style="left:213px;top:852px;width:245px">COMMENTARY</div>
    <div class="abs ph" style="left:213px;top:872px;width:245px;height:136px;background:linear-gradient(180deg,#d3393b,#c73436 70%,#eee)" role="img" aria-label="Illustration of the president surrounded by speech bubbles"></div>
    <span class="abs" style="left:215px;top:950px;background:#c8102e;color:#fff;font-size:5.5px;padding:1px 3px">VIDEO</span>
    <p class="abs" style="left:213px;top:966px;width:245px;height:42px;background:rgba(255,255,255,.82);font-size:14px;line-height:18px;padding:2px 5px">The two-word phrase President Vosk relies on most</p>
  </section>

  <aside class="ad-block">
    <div class="abs ad" role="img" aria-label="Illustration of a whale and a small plane in the sky"></div>
    <p class="abs ad-copy">Images you need,<br>at prices you love!</p>
    <div class="abs ad-dot"></div>
    <span class="abs ad-brand">PixQuay</span>
    <span class="abs ad-btn">Visit us ›</span>
    <span class="abs ad-note">Advertisement</span>
  </aside>
</main>

<footer>
  <div class="abs foot">
    <div class="foot-col"><h3>Regions</h3>U.S.<br>Africa<br>Americas<br>Asia<br>China<br>Europe<br>Middle<br>East<br>Opinion</div>
    <div class="foot-col"><h3>MONEY</h3>Business<br>Markets<br>Tech<br>Luxury</div>
    <div class="foot-col"><h3>ENTERTAINMENT</h3>Stars<br>Screen<br>Binge<br>Culture<br>Media</div>
    <div class="foot-col"><h3>TECH</h3>Business<br>Culture<br>Gadgets<br>Future<br>Startups</div>
    <div class="foot-col"><h3>SPORT</h3>Football<br>Golf<br>Tennis<br>Motorsport<br>Horseracing<br>Equestrian<br>Sailing<br>Skiing</div>
    <div class="foot-col"><h3>TRAVEL</h3>Travel<br>Aviation<br>Business<br>Traveller<br>Destinations<br>Features<br>Food/Drink<br>Hotels<br>Partner Hotels</div>
    <div class="foot-col"><h3>HEALTH</h3>Diet + Fitness<br>Living Well<br>Parenting + Family<br>Vital Signs</div>
    <div class="foot-col"><h3>FEATURES</h3>Freedom<br>Project<br>Impact<br>Your World<br>Inside<br>Africa2 degrees<br>All Features</div>
  </div>
  <div class="abs legal">© 2017 NorthDesk Meridian Broadcasting Group, Inc. All Rights Reserved.<br>NorthDesk ™ &amp; © 2016 NorthDesk<br>Terms of UsePrivacy Policy AdChoices Advertise with us About us Newsletters Work for us Help Transcripts License Footage NorthDesk.</div>
</footer>
</body>
</html>
```